Modern Business Card For A Digital Advertising Company

I'll be print on the Tarn Prints Velour paper http://us.tarnprints.example/products/velour/business-cards.html
Need's to be modern and use the color palette of the logo or gray scales. I think integrating the pixelation of the logo in to the card and having it wrap from one side to the other could be interesting. My company provides ad operations, web development, and number of other services to websites around the world. You can see my website at http://www.pixelharbor.example
Contact info on the card needs to have
Dana Welloby
President
p.555.318.4406
dana@pixelharbor.example
http://www.pixelharbor.example
Doesn't necessarily need to be in that order
Target Market(s)
Website owners
Industry/Entity Type
Business
Look and feel

```html
<!DOCTYPE html>
<html lang="en">
<head>
<meta charset="utf-8">
<title>Pixel Harbor Business Card</title>
<link rel="stylesheet" href="https://fonts.googleapis.com/css2?family=Exo+2:wght@400;600;700&display=swap">
<style>
  :root {
    --backdrop: #e4e4e4;
    --card: #ffffff;
    --ink: #3a3a3a;
    --ink-soft: #5a5a5a;
    --green: #7fbf3a;
    --green-light: #a6d46e;
    --band-dark: #4a4c4a;
  }
  * { box-sizing: border-box; margin: 0; padding: 0; }
  html, body {
    width: 1200px;
    height: 861px;
    overflow: hidden;
    background: var(--backdrop);
  }
  .business-card {
    position: absolute;
    left: 150px;
    top: 173px;
    width: 900px;
    height: 514px;
    background: var(--card);
    box-shadow: 0 6px 24px rgba(0,0,0,0.12);
    font-family: "Exo 2", sans-serif;
    overflow: hidden;
  }
  .brand {
    position: absolute;
    left: 84px;
    top: 150px;
    display: flex;
    align-items: center;
    gap: 16px;
  }
  .brand-mark {
    width: 44px;
    height: 44px;
    background: var(--green);
  }
  .brand-name {
    font-weight: 700;
    font-size: 46px;
    line-height: 1;
    color: var(--green);
    letter-spacing: 1px;
    text-transform: uppercase;
  }
  .identity {
    position: absolute;
    right: 96px;
    top: 78px;
    text-align: right;
  }
  .person-name {
    font-weight: 700;
    font-size: 40px;
    letter-spacing: 1.5px;
    color: var(--ink);
    text-transform: uppercase;
    line-height: 1;
  }
  .person-title {
    margin-top: 6px;
    font-weight: 600;
    font-size: 20px;
    letter-spacing: 1.5px;
    color: var(--ink-soft);
    text-transform: uppercase;
  }
  .contact-list {
    position: absolute;
    right: 96px;
    top: 188px;
    list-style: none;
  }
  .contact-item {
    display: flex;
    justify-content: flex-end;
    align-items: center;
    gap: 14px;
    height: 38px;
    font-size: 21px;
    color: var(--ink-soft);
    letter-spacing: 0.5px;
  }
  .contact-icon {
    width: 28px;
    height: 28px;
    background: var(--green);
    display: block;
    flex: none;
  }
  .band-dark {
    position: absolute;
    left: 0;
    top: 396px;
    width: 100%;
    height: 15px;
    background: var(--band-dark);
  }
  .band-green {
    position: absolute;
    left: 0;
    top: 421px;
    width: 100%;
    height: 93px;
    background: linear-gradient(90deg, var(--green) 0%, var(--green) 45%, var(--green-light) 100%);
  }
</style>
</head>
<body>
  <main class="business-card">
    <div class="brand">
      <span class="brand-mark"></span>
      <span class="brand-name">Pixel Harbor</span>
    </div>

    <div class="identity">
      <h1 class="person-name">Dana Welloby</h1>
      <p class="person-title">President</p>
    </div>

    <ul class="contact-list">
      <li class="contact-item">
        <span>555.318.4406</span>
        <svg class="contact-icon" viewBox="0 0 28 28" aria-hidden="true">
          <rect width="28" height="28" fill="#7fbf3a"/>
          <path d="M8 19 L11 22 L21 9 L19 7 L17 9 L18 11 L12 18 L10 17 Z" fill="#fff"/>
        </svg>
      </li>
      <li class="contact-item">
        <span>dana@pixelharbor.example</span>
        <svg class="contact-icon" viewBox="0 0 28 28" aria-hidden="true">
          <rect width="28" height="28" fill="#7fbf3a"/>
          <rect x="6" y="8" width="16" height="12" fill="#fff"/>
          <path d="M6 8 L14 15 L22 8" fill="none" stroke="#7fbf3a" stroke-width="1.5"/>
        </svg>
      </li>
      <li class="contact-item">
        <span>www.pixelharbor.example</span>
        <svg class="contact-icon" viewBox="0 0 28 28" aria-hidden="true">
          <rect width="28" height="28" fill="#7fbf3a"/>
          <rect x="6" y="7" width="16" height="11" fill="none" stroke="#fff" stroke-width="2"/>
          <rect x="10" y="20" width="8" height="2" fill="#fff"/>
        </svg>
      </li>
    </ul>

    <div class="band-dark"></div>
    <div class="band-green"></div>
  </main>
</body>
</html>
```